Property Developer - Simple yet Sophisticated and Sharp Business Card

We are a medium sized property developer involved mainly in townhouse developments and land subdivisions.

The company is looking for a simple, sharp and sophisticated business card that will be given to contractors, land owners, financiers etc and thus will need to look professional.

Property development related graphics and art can be used, however the card is not to be too "busy" or crowded. Our company name is KL Estates which could possibly be incorporated into the graphics or artwork.

Single sided and/or double sided designs will be acceptable.

A Simple, Sophisticated, Sharp design please!

Good Luck !

```html
<!DOCTYPE html>
<html lang="en">
<head>
<meta charset="utf-8">
<title>KL Estates — Business Card</title>
<link rel="stylesheet" href="https://fonts.googleapis.com/css2?family=Jost:wght@300;400;700&display=swap">
<style>
  :root {
    --page: #d3d7db;
    --card-light: #fdfbf8;
    --card-mid: #f1e9df;
    --card-warm: #e2d3c0;
    --gold: #c88a2c;
    --ink: #161616;
    --icon: #2a2a2a;
  }
  * { margin: 0; padding: 0; box-sizing: border-box; }
  html, body {
    width: 1048px; height: 1200px; overflow: hidden;
    background: var(--page);
  }
  .sheet {
    position: relative; width: 1048px; height: 1200px;
  }
  .card {
    position: absolute; left: 15px; width: 1018px; height: 580px;
    border-radius: 26px; overflow: hidden;
    background: var(--card-light);
    box-shadow: 0 0 0 2px #c4c8cc;
  }
  .card--front { top: 14px; }
  .card--back { top: 606px; }
  .card-art {
    position: absolute; inset: 0;
    background:
      radial-gradient(ellipse 60% 70% at 35% 35%, rgba(255,255,255,0.9), rgba(255,255,255,0) 70%),
      linear-gradient(115deg, var(--card-light) 0%, var(--card-mid) 45%, var(--card-light) 60%, var(--card-warm) 100%);
  }
  .brand {
    position: absolute; left: 70px; top: 92px;
    display: flex; align-items: center; gap: 26px;
  }
  .brand-mark {
    width: 150px; height: 150px; border-radius: 50%;
    background: var(--gold);
  }
  .brand-name {
    font-family: "Jost", sans-serif; font-weight: 700;
    font-size: 62px; letter-spacing: 1px; color: var(--ink);
    line-height: 1;
  }
  .person {
    position: absolute; left: 112px; top: 420px;
    text-align: right; width: 320px;
    font-family: "Jost", sans-serif; color: var(--gold);
  }
  .person-name {
    font-weight: 300; font-size: 48px; line-height: 1; letter-spacing: 0.5px;
    text-align: left;
  }
  .person-role {
    font-weight: 400; font-size: 15px; letter-spacing: 0.5px;
    color: var(--ink); margin-top: 4px; padding-right: 0;
    text-align: right; width: 300px;
  }
  .contact {
    position: absolute; left: 458px; top: 396px;
    list-style: none;
    font-family: "Jost", sans-serif; font-size: 21px; color: var(--ink);
  }
  .contact li {
    display: flex; align-items: center; gap: 14px; height: 34px;
    text-transform: uppercase;
  }
  .contact svg { width: 22px; height: 20px; fill: var(--icon); flex: none; }
</style>
</head>
<body>
<main class="sheet">
  <section class="card card--front">
    <div class="card-art" role="img" aria-label="Soft cream pattern of raised architectural blocks and a fine grid"></div>
    <div class="brand">
      <span class="brand-mark"></span>
      <span class="brand-name">KL ESTATES</span>
    </div>
    <div class="person">
      <p class="person-name">DANIEL MARSH</p>
      <p class="person-role">GENERAL MANAGER</p>
    </div>
    <ul class="contact">
      <li><svg viewBox="0 0 22 20"><rect x="1" y="2" width="20" height="16" rx="2"/><rect x="4" y="5" width="14" height="6" fill="#fff"/></svg>+ (07) 3000 1274</li>
      <li><svg viewBox="0 0 22 20"><rect x="5" y="1" width="12" height="6"/><rect x="1" y="8" width="20" height="8" rx="2"/><rect x="5" y="13" width="12" height="6" fill="#fff" stroke="#2a2a2a" stroke-width="1.5"/></svg>+ (07) 3000 5508</li>
      <li><svg viewBox="0 0 22 20"><rect x="1" y="3" width="20" height="14"/><path d="M1 3 L11 11 L21 3" fill="none" stroke="#fff" stroke-width="1.6"/></svg>projects.klestates@mailbox.example</li>
      <li><svg viewBox="0 0 22 20"><path d="M11 1 C6 1 3 4.5 3 8.5 C3 13 11 19 11 19 C11 19 19 13 19 8.5 C19 4.5 16 1 11 1 Z"/><circle cx="11" cy="8.5" r="3" fill="#fff"/></svg>PO Box 1200 Riverside QLD 4000</li>
    </ul>
  </section>

  <section class="card card--back">
    <div class="card-art" role="img" aria-label="Soft cream pattern of raised architectural blocks and a fine grid"></div>
    <div class="brand">
      <span class="brand-mark"></span>
      <span class="brand-name">KL ESTATES</span>
    </div>
    <div class="person">
      <p class="person-name">DANIEL MARSH</p>
      <p class="person-role">GENERAL MANAGER</p>
    </div>
    <ul class="contact">
      <li><svg viewBox="0 0 22 20"><rect x="1" y="2" width="20" height="16" rx="2"/><rect x="4" y="5" width="14" height="6" fill="#fff"/></svg>+ (07) 3000 1274</li>
      <li><svg viewBox="0 0 22 20"><rect x="5" y="1" width="12" height="6"/><rect x="1" y="8" width="20" height="8" rx="2"/><rect x="5" y="13" width="12" height="6" fill="#fff" stroke="#2a2a2a" stroke-width="1.5"/></svg>+ (07) 3000 5508</li>
      <li><svg viewBox="0 0 22 20"><rect x="1" y="3" width="20" height="14"/><path d="M1 3 L11 11 L21 3" fill="none" stroke="#fff" stroke-width="1.6"/></svg>projects.klestates@mailbox.example</li>
      <li><svg viewBox="0 0 22 20"><path d="M11 1 C6 1 3 4.5 3 8.5 C3 13 11 19 11 19 C11 19 19 13 19 8.5 C19 4.5 16 1 11 1 Z"/><circle cx="11" cy="8.5" r="3" fill="#fff"/></svg>PO Box 1200 Riverside QLD 4000</li>
    </ul>
  </section>
</main>
</body>
</html>
```